Letterhead for Dorian Welk

I need a letterhead based on the business card design

Industry/Entity Type

Business

Requirements
Must have
• Footer: Dorian Welk Naturopath
Shop 4123c, 46 Carrow Lane, Sydney 2000

```html
<!DOCTYPE html>
<html lang="en">
<head>
<meta charset="utf-8">
<title>Dorian Welk Naturopathy – Letterhead</title>
<link rel="stylesheet" href="https://fonts.googleapis.com/css2?family=Montserrat:wght@400;700&display=swap">
<style>
  :root {
    --orange: #f0952a;
    --orange-deep: #ec8a1c;
    --orange-soft: #f7c58a;
    --orange-pale: #fbe3c7;
    --paper: #ffffff;
    --white: #ffffff;
  }
  * { margin: 0; padding: 0; box-sizing: border-box; }
  html, body { width: 857px; height: 1200px; overflow: hidden; background: var(--paper); }
  .letterhead {
    position: relative;
    width: 857px;
    height: 1200px;
    background: var(--paper);
    font-family: "Montserrat", Arial, sans-serif;
    overflow: hidden;
  }
  .header-shape { position: absolute; top: 0; left: 0; width: 857px; height: 340px; }
  .brand-mark {
    position: absolute; top: 40px; left: 52px;
    width: 110px; height: 110px; border-radius: 50%;
    background: var(--orange-soft); opacity: 0.55;
  }
  .brand {
    position: absolute; top: 88px; left: 330px; width: 380px;
    color: var(--white); text-align: center;
  }
  .brand-name {
    font-size: 50px; font-weight: 700; letter-spacing: 2px; line-height: 1;
  }
  .brand-rule { height: 2px; background: var(--white); margin: 12px -20px 8px; }
  .brand-field {
    font-size: 17px; font-weight: 400; letter-spacing: 8px; line-height: 1.2;
  }
  .brand-contact {
    margin-top: 6px; font-size: 9px; letter-spacing: 1px; word-spacing: 14px;
  }
  .backdrop {
    position: absolute; left: 150px; bottom: 80px; width: 560px; height: 530px;
    border-radius: 50% 50% 0 0 / 70% 70% 0 0;
    background: radial-gradient(ellipse at 50% 70%, var(--orange-pale) 0%, rgba(251,227,199,0.5) 55%, rgba(255,255,255,0) 80%);
  }
  .footer-band {
    position: absolute; left: 0; bottom: 80px; width: 857px; height: 40px;
    background: rgba(247,197,138,0.55);
    display: flex; align-items: center; justify-content: center;
  }
  .footer-address {
    color: var(--white); font-size: 11px; letter-spacing: 0.5px;
  }
  .footer-bar {
    position: absolute; left: 0; bottom: 40px; width: 857px; height: 40px;
    background: var(--orange-deep);
  }
</style>
</head>
<body>
<main class="letterhead">
  <svg class="header-shape" viewBox="0 0 857 340" aria-hidden="true">
    <path d="M0 0 H857 V330 C820 250 760 215 660 205 C520 190 380 215 240 215 C130 215 50 195 0 175 Z" fill="var(--orange-soft)" opacity="0.55"/>
    <path d="M0 0 H857 V235 C800 205 720 190 620 185 C480 178 360 200 230 200 C120 200 45 185 0 165 Z" fill="var(--orange)"/>
    <path d="M857 20 C760 60 700 140 700 240 C740 200 800 190 857 200 Z" fill="var(--orange-soft)" opacity="0.45"/>
  </svg>

  <div class="brand-mark" aria-hidden="true"></div>

  <header class="brand">
    <h1 class="brand-name">DORIAN WELK</h1>
    <div class="brand-rule"></div>
    <p class="brand-field">NATUROPATHY</p>
    <p class="brand-contact">dorianwelk.com.au hello@dorianwelk.com.au</p>
  </header>

  <div class="backdrop" role="img" aria-label="Faint layered leaf backdrop in pale orange"></div>

  <footer>
    <div class="footer-band">
      <p class="footer-address">Dorian Welk Naturopath · Shop 4123c, 46 Carrow Lane, Sydney 2000</p>
    </div>
    <div class="footer-bar"></div>
  </footer>
</main>
</body>
</html>
```